To design the Curriculum Vitae of a General Manager Legal

the objective is to redesign the attached Résumé for a senior level Internal Legal Executive in order to make it attractive, easily readable, catchy, modern looking while staying classy, elegant, sobre, and serious.
The résumé is attached to this project. it contains the followings sections : Photo; Contact Details; Summary; Education; Experience; Other.
Feel free to use photoshop to improve photo.
Updates

Target Market(s)

Legal community; law firms; Big corporations requiring internal legal senior executive

Font styles to use
Serif

Colors
ffffff
85cae6
33a6d7
0292cd
86cfc6
cfeae6
757575
919191
d9d9d9

Requirements
Must have
• classy; serious; professional; elegant; easy to read; catchy; modern;

```html
<!DOCTYPE html>
<html lang="en">
<head>
<meta charset="utf-8">
<title>Curriculum Vitae – Leila Haddad Karam</title>
<link rel="stylesheet" href="https://fonts.googleapis.com/css2?family=Andada+Pro:wght@400;700&display=swap">
<style>
:root{
  --backdrop:#bfc0cc;
  --paper:#ffffff;
  --ink:#2b4c9c;
  --ink-dark:#1d3f8f;
  --panel:#e6eaf2;
  --tab:#dfe6ef;
  --text:#3a3a3a;
  --muted:#555555;
}
*{margin:0;padding:0;box-sizing:border-box}
html,body{width:1200px;height:842px;overflow:hidden;background:var(--backdrop)}
body{position:relative;font-family:"Andada Pro",Georgia,serif}
.page{position:absolute;top:64px;width:550px;height:720px;background:var(--paper);overflow:hidden;box-shadow:0 2px 10px rgba(0,0,0,.12)}
.page--front{left:45px;width:549px}
.page--back{left:616px}

.cv-title{position:absolute;top:58px;left:0;right:0;text-align:center;color:var(--ink);font-size:16px;font-weight:400;letter-spacing:15px;padding-left:14px;line-height:20px}
.portrait{position:absolute;left:237px;top:113px;width:80px;height:89px;border-radius:12px;background:linear-gradient(160deg,#6b5747,#b99a86 55%,#4b3c33)}
.identity{position:absolute;top:211px;left:0;right:0;text-align:center;color:var(--ink)}
.identity__name{font-size:17px;font-weight:400;line-height:22px}
.identity__name b{font-weight:700;color:var(--ink-dark)}
.identity__contact{font-size:13px;margin-top:3px}

.summary{position:absolute;left:23px;top:286px;width:506px;height:434px;background:var(--panel)}
.tab{position:absolute;font-weight:700;color:var(--ink-dark)}
.summary .tab{left:0;top:19px;width:122px;height:27px;background:var(--paper);font-size:15px;line-height:27px;padding-left:44px}
.summary__text{position:absolute;left:44px;top:66px;width:446px;column-count:2;column-gap:11px;color:var(--ink);font-size:9.4px;line-height:16.2px}
.summary__text p+p{text-indent:12px}

.section-tab{position:absolute;left:0;width:142px;height:24px;background:var(--tab);font-size:13.5px;line-height:24px;text-align:right;padding-right:18px}
.section-tab--edu{top:33px}
.section-tab--exp{top:148px}

.entries{position:absolute;left:0;width:550px}
.entry{display:flex;font-size:10.4px;line-height:13px;color:var(--text)}
.entry__date{width:151px;text-align:right;padding-right:14px;flex:none}
.entry__what{white-space:nowrap}
.entry__what b{color:var(--ink-dark);font-size:11px}
.edu{top:65px}
.edu .gap{height:4px}
.exp{top:174px}
.exp .entry{font-size:11.2px;line-height:17px}
.exp .entry__what b{font-size:12px}

.duties{position:absolute;left:150px;top:214px;width:378px;font-size:7.4px;line-height:9.4px;color:var(--muted)}
.duties h4{font-size:7.6px;color:#111;font-weight:700;margin-top:1px}
.duties ul{list-style:none}
.duties li{position:relative;padding-left:11px;margin-bottom:2px}
.duties li::before{content:"";position:absolute;left:2px;top:3.5px;width:3px;height:3px;border-radius:50%;background:#333}
</style>
</head>
<body>

<section class="page page--front">
  <h1 class="cv-title">CURRICULUM VITAE</h1>
  <div class="portrait" role="img" aria-label="Portrait photo of Leila Haddad Karam"></div>
  <header class="identity">
    <div class="identity__name">Leila <b>Haddad Karam</b></div>
    <div class="identity__contact">Mobile : +971 50 0000147 &nbsp;|&nbsp; Mail : leila.haddad@mailbox.example</div>
  </header>

  <div class="summary">
    <h2 class="tab">Summary</h2>
    <div class="summary__text">
      <p>A senior qualified legal professional with more than 15 years of experience in private practice and in-house focusing on the following industries: Real Estate, Retail and Services, obtained in UAE, France and Syria. Practice transactional skills (M&amp;A, real estate, commercial, corporate restructuring, strategic funding), organizational skills (policies and procedures and authority matrix covering different contexts in corporate environment), lawyering skills (preemptive legal advice, and a multi jurisdiction litigation management expertise), managerial skills (enhancing the value add of the legal department as both a service provider and a risk gatekeeper).</p>
      <p>A senior qualified legal professional with more than 15 years of experience in private practice and in-house focusing on the following industries: Real Estate, Retail and Services, obtained in UAE, France and Syria. Practice transactional skills (M&amp;A, real estate, commercial, corporate restructuring, strategic funding), organizational skills (policies and procedures and authority matrix covering different contexts in corporate environment), lawyering skills (preemptive legal advice, and a multi jurisdiction litigation management expertise), managerial skills (enhancing the value add of the legal department as both a service provider and a risk gatekeeper).</p>
      <p>Prior to moving to Dubai, I have lived in Paris France, where I have worked in various organizations including the Northbridge Arbitration Centre, a billing software company and a consultancy practice. I graduated from University of Saint-Clément with two Master Degrees.</p>
      <p>Mother of three, I am passionate about Bon Fide work towards Women Empowerment and Refugee Children Education.</p>
    </div>
  </div>
</section>

<section class="page page--back">
  <h2 class="tab section-tab section-tab--edu">Education</h2>
  <div class="entries edu">
    <div class="entry"><span class="entry__date"></span><span class="entry__what"><b>Université Saint-Clément, Paris, France</b></span></div>
    <div class="entry"><span class="entry__date">1998 – 99</span><span class="entry__what">Master degree in Litigation, Arbitration, and Alternative Dispute Resolution</span></div>
    <div class="entry"><span class="entry__date">1997 – 98</span><span class="entry__what">Master degree in commercial law</span></div>
    <div class="gap"></div>
    <div class="entry"><span class="entry__date">1997 – 98</span><span class="entry__what"><b>Institute of Legal Studies Paris, France</b></span></div>
    <div class="entry"><span class="entry__date">1992 – 96</span><span class="entry__what"><b>Levant University, Syria</b></span></div>
    <div class="entry"><span class="entry__date"></span><span class="entry__what">Law degree</span></div>
  </div>

  <h2 class="tab section-tab section-tab--exp">Experience</h2>
  <div class="entries exp">
    <div class="entry"><span class="entry__date">April 2017 – Present</span><span class="entry__what"><b>General Manager Legal at Noor Group – Verdant (“NGV”)</b></span></div>
    <div class="entry"><span class="entry__date">May 2015 – April 2017</span><span class="entry__what"><b>Senior Legal Counsel at Noor Group Verdant Retail</b></span></div>
  </div>

  <div class="duties">
    <h4>Description of Position</h4>
    <p>Lead and manage the legal, compliance, functions and risk management function for NGV operations in Syria, Lebanon, Jordan, Iraq, Egypt, Georgia, Armenia and Pakistan (“Countries”). A Legal Business Partner to drive business development agenda (organically, M&amp;A, digital/ecommerce), and contribute to functional strategies.</p>
    <h4>Key Responsibilities</h4>
    <ul>
      <li>Develop and execute the legal strategy and plans in alignment with strategic objectives of the company.</li>
      <li>Lead the Legal team across the Countries: attract, develop, assess and engage the right legal talents.</li>
      <li>Coordinating with management and Head of business units, evaluating strategy and merits and or progress of specific projects.</li>
      <li>Manage and coordinate the Company’s approach towards litigation to ensure cost effectiveness including negotiations of contracts with outside legal firms, monitor quality of work and delivery.</li>
    </ul>
    <h4>M&amp;A</h4>
    <ul><li>Contribute to M&amp;A and prospective acquisitions activities, perform due diligence, terms negotiations, closing and post-closing tasks.</li></ul>
    <h4>Business Development/Partnership</h4>
    <ul>
      <li>Lead &amp; implement the legal expansion plans in Countries including setting up new legal entities, due diligence, and risk matrix.</li>
      <li>Prepare and structure complex contract negotiations. Examine intricate agreements and other documents for accuracy, legality and conformity with business standards.</li>
      <li>Oversee the legal process Prepare and review agreements, contracts regarding commercial, development and business transactions: Memoranda of Understanding, Agreements to Lease and Lease Agreement, JVs, Franchise Agreements, Consultancy Agreements, Tender Documentation, Procurement Agreements, Mergers and Acquisitions, and other related to the development of company’s business in the Countries.</li>
    </ul>
    <h4>Digital</h4>
    <ul><li>Perform all the legal aspects of NGV digital and ecommerce projects.</li></ul>
    <h4>Corporate Governance &amp; Compliance</h4>
    <ul>
      <li>Create and secure protection of Intellectual property.</li>
      <li>Ensure the application of NGV corporate policies.</li>
      <li>Collaborate with the tax and finance groups to determine appropriate corporate structure.</li>
      <li>Communicate latest regulatory requirements to Business Units.</li>
      <li>Develop and maintain legal processes and business transactions compliance and related training; Provide support for governmental relations and regulatory affairs activities.</li>
    </ul>
    <h4>Risk Management</h4>
    <ul>
      <li>Lead the implementation of risk control measures, contractual obligations and the structuring of transactions.</li>
      <li>Lead the implementation of risk control measures, contractual obligations and the structuring of transactions.</li>
    </ul>
    <h4>Others</h4>
    <ul>
      <li>Review and negotiate (in conjunction with the Treasury department) of financial documentation required to satisfy the funding, banking and other monetary services’ requirements of the company.</li>
      <li>For new jurisdictions: Carry out legal research, due diligence procedures, prepare corporate documents and other formalities for the relevant operating companies. Establish methods to accomplish business goals whilst minimizing legal and commercial risks.</li>
      <li>Prepare board papers and updates to senior management</li>
    </ul>
  </div>
</section>

</body>
</html>
```